12 Week Brisk Peak Lean Form Challenge Flyer

Hi,
We are a tennis coaching business called Vantle Racquet based in Sydney Australia. We are looking to launch a new 12 week fitness program called "12 Week Brisk Peak Form Lean Challenge"
We would like the flyer to utilise the colours green and yellow reflecting the tennis theme - however we don't necessarily want it to look like a tennis flyer as tennis is only a small piece of the program via our tennis cardio workouts. We are using tennis cardio as a fitness thing.
We are based in Australia where spring is about to start and everyone is looking to get fit and beach ready for summer so we would like the flyer to communicate fitness, energy, vitality etc. = a Brisk Peak Life !
SPECIFICALLY ON THE FLYER WE WOULD LIKE THE FOLLOWING INFO:
Get a Brisk Peak Form. Live a Brisk Peak Life. In Just 12 Weeks.
Take the challenge today !
Your challenge should you choose to accept it will include:
3 weekly 1hr group training sessions using fast, high intensity & seriously fun cardio workouts. with music to pump you up.
90 Day weight management & nutrition plan using revolutionary nutritional, all natural products. (All products included)
12 Week E-Course covering the dieting dilemma, exercise, stress management and sleep.
Personalised & interactive online membership program which includes:
- Customised meal plans based on your personal nutrition parameters & food preferences
- Step by Step guide to achieving your health goals
- Interactive goal setting charts to track your progress
- Delicious recipe database & thousands of meal options
- Easy interactive nutrition and exercise journal
- Full nutrition support from our team of experts
It's time to take action & get Brisk Peak Form Lean !
Only $99 per week !!
Join TODAY
Starts September 17th.
Call 02 7381 2459 or email us at info@vantleracquet.example
Please let us know if you need any more info.
Our website is www.vantleracquet.example if you want to see more about us but again please keep in mind this is not being marketed as a tennis specific program ... more of a fitness, get ready for summer program.
Thanks
Gwendolyn
Target Market(s)
Men and women between ages of 27-45 years
Industry/Entity Type
Nutrition

```html
<!DOCTYPE html>
<html lang="en">
<head>
<meta charset="utf-8">
<title>12 Week Brisk Peak Form Lean Challenge – Flyer</title>
<link href="https://fonts.googleapis.com/css2?family=Oswald:wght@600;700&family=Source+Sans+3:ital,wght@0,400;0,600;0,700;1,600&family=Crimson+Text&display=swap" rel="stylesheet">
<style>
  :root {
    --green-deep: #0f7a2e;
    --green-mid: #5fae2a;
    --green-light: #9bcf2e;
    --lime: #c9e21c;
    --yellow: #fff200;
    --yellow-soft: #f6ee3a;
    --ink: #2b2b2b;
    --white: #ffffff;
    --stage: #ecece6;
  }
  * { margin: 0; padding: 0; box-sizing: border-box; }
  html, body { width: 1200px; height: 750px; overflow: hidden; background: var(--stage); }
  .canvas { position: relative; width: 1200px; height: 750px; }

  .card { position: absolute; overflow: hidden; box-shadow: 0 6px 18px rgba(0,0,0,.25); }
  .card-bg { position: absolute; inset: 0; width: 100%; height: 100%; }

  /* Front card */
  .front { left: 272px; top: 35px; width: 335px; height: 680px; }
  .front-title {
    position: absolute; top: 36px; left: 0; right: 0; text-align: center;
    font-family: "Oswald", "Arial Narrow", sans-serif; font-weight: 700;
    font-size: 31px; line-height: 1.08; color: var(--green-deep); letter-spacing: .2px;
  }
  .front-title .accent { color: var(--yellow); }
  .tagline {
    position: absolute; left: 42px; top: 415px; width: 176px; height: 176px;
    display: flex; align-items: center; justify-content: center; text-align: center;
    font-family: "Source Sans 3", Arial, sans-serif; font-size: 19px; line-height: 1.2;
    color: #111; text-transform: uppercase;
  }
  .tagline .highlight { color: var(--green-deep); }
  .cta {
    position: absolute; top: 608px; left: 0; right: 0; text-align: center;
    font-family: "Oswald", "Arial Narrow", sans-serif; font-weight: 700;
    font-size: 22px; color: var(--green-deep);
  }
  .website {
    position: absolute; top: 648px; left: 0; right: 0; text-align: center;
    font-family: "Crimson Text", Georgia, serif; font-size: 16px; color: #222;
  }

  /* Back card */
  .back { left: 622px; top: 45px; width: 320px; height: 660px; }
  .back-title {
    position: absolute; top: 38px; left: 22px; right: 12px;
    font-family: "Oswald", "Arial Narrow", sans-serif; font-weight: 700;
    font-size: 30px; line-height: 1.05; color: var(--white);
  }
  .details {
    position: absolute; top: 118px; left: 20px; right: 18px;
    font-family: "Source Sans 3", Arial, sans-serif; font-size: 12.4px; line-height: 1.18;
    color: var(--ink); text-align: justify;
  }
  .details ul { list-style: none; }
  .details li { position: relative; padding-left: 8px; }
  .details li::before { content: "•"; position: absolute; left: 0; }
  .details p { margin-top: 4px; }
  .action {
    position: absolute; top: 452px; left: 20px; right: 38px;
    border-top: 1px solid #333; border-bottom: 1px solid #333; padding: 3px 0 4px;
    font-family: "Source Sans 3", Arial, sans-serif; font-size: 16px; line-height: 1.1;
    color: var(--ink); text-transform: uppercase;
  }
  .price {
    position: absolute; top: 505px; left: 20px;
    font-family: "Source Sans 3", Arial, sans-serif; font-weight: 700; font-size: 16px;
    color: var(--green-deep);
  }
  .start {
    position: absolute; top: 527px; left: 20px;
    font-family: "Source Sans 3", Arial, sans-serif; font-weight: 600; font-style: italic;
    font-size: 10.5px; color: var(--green-deep);
  }
  .contact-band {
    position: absolute; top: 555px; left: 0; right: 0; height: 66px;
    background: var(--green-deep); padding: 8px 0 0 16px;
    font-family: "Source Sans 3", Arial, sans-serif; color: var(--white);
  }
  .contact-band .phone { font-weight: 700; font-size: 21px; line-height: 1.1; }
  .contact-band .email { font-size: 15px; line-height: 1.2; }
</style>
</head>
<body>
<main class="canvas">

  <section class="card front" aria-label="Flyer front">
    <svg class="card-bg" viewBox="0 0 335 680" aria-hidden="true">
      <defs>
        <linearGradient id="front-fill" x1="0" y1="0" x2="0" y2="1">
          <stop offset="0" stop-color="#8fc92e"/>
          <stop offset=".35" stop-color="#b8dc2a"/>
          <stop offset=".55" stop-color="#eef01a"/>
          <stop offset="1" stop-color="#fff200"/>
        </linearGradient>
        <radialGradient id="photo-fill" cx=".5" cy=".45" r=".6">
          <stop offset="0" stop-color="#3f6a2a"/>
          <stop offset=".6" stop-color="#1d2a18"/>
          <stop offset="1" stop-color="#050805"/>
        </radialGradient>
      </defs>
      <rect width="335" height="680" fill="url(#front-fill)"/>
      <path d="M0 270 C 90 220, 220 200, 335 150 L335 175 C 230 225, 110 245, 0 300 Z" fill="#ffffff" opacity=".35"/>
      <path d="M0 330 C 120 300, 250 260, 335 200 L335 560 L0 560 Z" fill="#f5ef1c" opacity=".6"/>
      <circle cx="198" cy="338" r="148" fill="#7cbd2c"/>
      <circle cx="198" cy="338" r="138" fill="#fff200"/>
      <circle cx="198" cy="338" r="128" fill="#6ab22a"/>
      <circle cx="198" cy="338" r="118" fill="url(#photo-fill)" role="img" aria-label="Photo of a player striking a tennis ball with a racquet"/>
      <circle cx="130" cy="503" r="104" fill="#c7e22a"/>
      <circle cx="130" cy="503" r="96" fill="#5fae2a"/>
      <circle cx="130" cy="503" r="88" fill="#ffffff"/>
      <path d="M0 600 C 110 590, 230 575, 335 560" stroke="#ffffff" stroke-width="2" fill="none" opacity=".6"/>
      <line x1="70" y1="640" x2="265" y2="640" stroke="#6d8a1a" stroke-width="1"/>
    </svg>
    <h1 class="front-title"><span class="accent">12 WEEK</span> BRISK PEAK<br>LEAN FORM CHALLENGE</h1>
    <p class="tagline"><span>Get a Brisk Peak Form. Live a Brisk Peak Life. <span class="highlight">In just 12 weeks.</span></span></p>
    <p class="cta">TAKE THE CHALLENGE TODAY !</p>
    <p class="website">www.vantleracquet.example</p>
  </section>

  <section class="card back" aria-label="Flyer back">
    <svg class="card-bg" viewBox="0 0 320 660" aria-hidden="true">
      <defs>
        <linearGradient id="back-fill" x1="0" y1="0" x2="0" y2="1">
          <stop offset="0" stop-color="#7fbf2c"/>
          <stop offset=".3" stop-color="#b6d92a"/>
          <stop offset="1" stop-color="#e8ec22"/>
        </linearGradient>
      </defs>
      <rect width="320" height="660" fill="url(#back-fill)"/>
      <path d="M0 330 C 120 300, 230 250, 320 180 L320 660 L0 660 Z" fill="#fff200"/>
      <path d="M0 340 C 130 310, 240 260, 320 195" stroke="#ffffff" stroke-width="3" fill="none" opacity=".7"/>
      <rect y="621" width="320" height="14" fill="#c8e33a"/>
      <rect y="635" width="320" height="25" fill="#fff200"/>
    </svg>
    <h2 class="back-title">12 WEEK BRISK PEAK<br>FORM LEAN CHALLENGE</h2>
    <div class="details">
      <ul>
        <li>3 weekly 1hr group training sessions using fast, high intensity &amp; seriously fun cardio workouts, with music to pump you up.</li>
        <li>90 Day weight management &amp; nutrition plan using revolutionary nutritional, all natural products. (All products included)</li>
        <li>12 Week E-Course covering the dieting dilemma, exercise, stress management and sleep.</li>
      </ul>
      <p>Personalised &amp; interactive online membership program which includes:</p>
      <ul>
        <li>Customised meal plans based on your personal nutrition parameters &amp; food preferences</li>
        <li>Step by Step guide to achieving your health goals</li>
        <li>Interactive goal setting charts to track your progress</li>
        <li>Delicious recipe database &amp; thousands of meal options</li>
        <li>Easy interactive nutrition and exercise journal</li>
        <li>Full nutrition support from our team of experts</li>
      </ul>
    </div>
    <p class="action">It's time to take action &amp;<br>get Brisk Peak Form Lean !</p>
    <p class="price">ONLY $99 PER WEEK !!</p>
    <p class="start">Join Today • Starts September 17th.</p>
    <div class="contact-band">
      <p class="phone">CALL 02 7381 2459</p>
      <p class="email">or email us at info@vantleracquet.example</p>
    </div>
  </section>

</main>
</body>
</html>
```